Delivery Performance Dashboard for Web Portal

We need you to design a dashboard for our web portal. We deliver sand and stone to construction jobsites. The attached screenshot is from our current web portal dashboard . It shows how much material has been delivered from an order.

Dump trucks will deliver multiple loads during the day and the dispatcher uses the dashboard to monitor if they need to add more trucks or less trucks to fulfill the order. An example would be, I need to ship 1,000 tons of sand to a jobsite and I plan to use 10 trucks during the day and that it will take 10 hours of hauling to complete the job. After 5 hours of hauling (50% the day is over), I should have delivered 500 tons of sand (50% of the order). But maybe there is a lot of traffic, and I only have delivered 300 tons. The dashboard will show that I am behind schedule and I might need to add 2 more trucks to the job.

Industry/Entity Type

Construction

Font styles to use
Sans Serif

Requirements
Must have
• We need a progress bar showing how much material has been delivered, how much material was requested to be delivered total and how much material should have been delivered at the current time. The goal is to show the user if the deliveries are ahead or behind the expected pace and why.
Nice to have
• The icons for plant, driving and jobsite show if the actual times have exceeded or beaten the planned times. Maybe you have other ideas to show the user if the trucks are sitting longer on the jobsite, at the plant to get loaded or driving to and from the jobsite.

```html
<!DOCTYPE html>
<html lang="en">
<head>
<meta charset="utf-8">
<title>Dispatch Dashboard – Details Popup</title>
<link href="https://fonts.googleapis.com/css2?family=Montserrat:wght@400;500;600;700&display=swap" rel="stylesheet">
<style>
:root{
  --page:#ffffff;
  --app-bg:#f5f5f6;
  --surface:#ffffff;
  --ink:#1c1c24;
  --muted:#6b6b78;
  --line:#ececf0;
  --brand:#2b3ff0;
  --brand-soft:#e8ebff;
  --track:#e9ecfa;
  --pending:#f3b81f;
  --accepted:#1fd8a2;
  --good:#1ec45c;
  --bad:#f0345a;
  --icon:#5f6270;
  --amber-soft:#fcecc6;
  --amber:#f2b52e;
  --mint-soft:#c9f4e4;
  --mint:#26c993;
}
*{box-sizing:border-box;margin:0;padding:0}
html,body{width:1200px;height:675px;overflow:hidden;background:var(--page);font-family:"Montserrat",sans-serif;color:var(--ink)}
.app{position:absolute;left:150px;top:84px;width:900px;height:506px;background:var(--app-bg);border-radius:16px;overflow:hidden;box-shadow:0 6px 30px rgba(30,30,60,.06)}
.sidebar{position:absolute;left:0;top:0;width:37px;height:100%;background:var(--surface)}
.logo-mark{position:absolute;left:6px;top:7px;width:25px;height:25px;border-radius:3px;background:var(--brand)}
.nav-item{position:absolute;left:7px;width:24px;height:24px;display:flex;align-items:center;justify-content:center;border-radius:3px}
.nav-item.active{background:var(--brand-soft)}
.topbar{position:absolute;left:37px;top:0;right:0;height:37px;background:var(--surface)}
.user{position:absolute;right:40px;top:9px;display:flex;align-items:center;gap:5px;font-size:8px;font-weight:500}
.avatar{width:20px;height:20px;border-radius:3px;background:linear-gradient(135deg,#3a2b25,#1a1412)}
.stat{position:absolute;top:72px;width:380px;height:89px;background:var(--surface);border-radius:4px}
.stat .badge{position:absolute;left:7px;top:21px;width:26px;height:26px;border-radius:4px;display:flex;align-items:center;justify-content:center}
.stat .label{position:absolute;left:7px;top:59px;font-size:9.5px;font-weight:600}
.stat .value{position:absolute;right:16px;top:36px;font-size:15px;font-weight:700;letter-spacing:.5px}
.orders{position:absolute;left:66px;top:175px;width:768px;height:278px;background:var(--surface);border-radius:4px}
.th{position:absolute;top:16px;font-size:8.5px;font-weight:600}
.row{position:absolute;left:0;width:768px;height:33px;border-bottom:1px solid var(--line)}
.cell{position:absolute;top:50%;transform:translateY(-50%);font-size:6.6px;font-weight:500;white-space:nowrap}
.status{position:absolute;top:50%;transform:translateY(-50%);left:415px;width:47px;height:18px;border-radius:9px;color:#fff;font-size:6.6px;font-weight:600;display:flex;align-items:center;justify-content:center}
.status.pending{background:var(--pending)}
.status.accepted{background:var(--accepted)}
.tons{position:absolute;left:475px;top:8px;width:89px}
.bar{height:5px;border-radius:3px;background:var(--track);position:relative}
.bar i{position:absolute;left:0;top:0;height:5px;border-radius:3px;background:linear-gradient(90deg,#3a2ff0,#2b5bf5)}
.bar .dot{width:5px;border-radius:50%}
.tons-meta{display:flex;justify-content:space-between;font-size:5.5px;font-weight:500;margin-top:4px}
.waits{position:absolute;left:576px;top:50%;transform:translateY(-50%);display:flex;align-items:center;gap:3px}
.good{color:var(--good)} .bad{color:var(--bad)}
.pager{position:absolute;top:241px;left:0;width:100%;display:flex;justify-content:center;gap:2px}
.pg{width:23px;height:23px;border-radius:50%;display:flex;align-items:center;justify-content:center;font-size:7.5px;font-weight:500}
.pg.prev{background:#f1f1f3}
.pg.current{border:1px solid var(--brand);color:var(--brand)}
.pg.next{background:var(--brand)}
.popup{position:absolute;left:624px;top:145px;width:114px;height:131px;background:var(--surface);border-radius:3px;box-shadow:0 4px 16px rgba(20,20,50,.12);z-index:3;font-size:5.5px;font-weight:500}
.popup-head{height:15px;background:#f3f3f5;padding:4px 5px}
.popup-avg{height:27px;text-align:right;padding:10px 5px 0}
.popup-line{height:28px;border-top:1px solid var(--line);display:flex;align-items:center;justify-content:space-between;padding:0 5px}
.popup-line .name{display:flex;align-items:center;gap:4px;color:var(--muted)}
.popup-line .nums{text-align:right;line-height:1.5}
.caption{position:absolute;top:616px;width:100%;text-align:center;font-size:11.5px;font-weight:500;color:var(--brand);letter-spacing:.3px}
</style>
</head>
<body>
<main class="app">
  <aside class="sidebar">
    <div class="logo-mark"></div>
    <div class="nav-item active" style="top:90px"><svg width="10" height="10" viewBox="0 0 10 10" fill="none" stroke="#2b3ff0" stroke-width="1"><rect x=".5" y=".5" width="3.5" height="4.5"/><rect x="6" y=".5" width="3.5" height="3"/><rect x="6" y="5" width="3.5" height="4.5"/><rect x=".5" y="6.5" width="3.5" height="3"/></svg></div>
    <div class="nav-item" style="top:130px"><svg width="10" height="10" viewBox="0 0 10 10" fill="none" stroke="#2b3ff0" stroke-width="1"><circle cx="5" cy="3" r="2.2"/><path d="M1 9.5c.5-2.5 2-3.5 4-3.5s3.5 1 4 3.5"/></svg></div>
    <div class="nav-item" style="top:171px"><svg width="10" height="10" viewBox="0 0 10 10" fill="none" stroke="#2b3ff0" stroke-width="1"><rect x="1" y=".5" width="7" height="9"/><path d="M3 3h3M3 5h3M3 7h2M8 4h1.5v5.5"/></svg></div>
    <div class="nav-item" style="top:212px"><svg width="10" height="10" viewBox="0 0 10 10" fill="none" stroke="#2b3ff0" stroke-width="1"><rect x=".5" y="2" width="9" height="6.5" rx="1.5"/><circle cx="3.5" cy="5.5" r=".4"/><circle cx="6.5" cy="5.5" r=".4"/></svg></div>
    <div class="nav-item" style="top:252px"><svg width="10" height="10" viewBox="0 0 10 10" fill="none" stroke="#2b3ff0" stroke-width="1"><path d="M1.5 9.5V1h6l-1 2 1 2h-6"/></svg></div>
  </aside>

  <header class="topbar">
    <div class="user"><div class="avatar" role="img" aria-label="User profile photo"></div><span>Dana Whitfield</span><svg width="10" height="8" viewBox="0 0 10 8" style="margin-left:6px"><path d="M3 3l2 2 2-2" stroke="#2b3ff0" fill="none" stroke-width="1"/></svg></div>
  </header>

  <section class="stat" style="left:66px">
    <div class="badge" style="background:var(--amber-soft)"><svg width="10" height="10" viewBox="0 0 10 10"><rect x="3" y="1" width="6" height="6" fill="var(--amber)"/><rect x="1" y="3" width="6" height="6" fill="#f6c85a" stroke="var(--amber-soft)" stroke-width=".8"/></svg></div>
    <div class="label">Pending Orders</div>
    <div class="value">05</div>
  </section>
  <section class="stat" style="left:454px">
    <div class="badge" style="background:var(--mint-soft)"><svg width="10" height="10" viewBox="0 0 10 10"><rect x="3" y="1" width="6" height="6" fill="var(--mint)"/><rect x="1" y="3" width="6" height="6" fill="#57d9ac" stroke="var(--mint-soft)" stroke-width=".8"/><path d="M2.5 6l1.2 1.2 2-2.2" stroke="#fff" fill="none" stroke-width=".8"/></svg></div>
    <div class="label">Active Travelers</div>
    <div class="value">345</div>
  </section>

  <section class="orders">
    <div class="th" style="left:7px">Order #</div>
    <div class="th" style="left:56px">Origin</div>
    <div class="th" style="left:145px">Destination</div>
    <div class="th" style="left:271px">Customer</div>
    <div class="th" style="left:415px">Status</div>
    <div class="th" style="left:476px">Tons</div>
    <div class="th" style="left:577px">Wait Times</div>
    <div class="th" style="left:666px">Remaining</div>
    <div class="th" style="left:741px;display:flex;align-items:center;gap:2px;font-size:5px">+/-<svg width="11" height="8" viewBox="0 0 11 8"><path d="M0 1h6.5v5H0zM6.5 2.5h2.5l2 2V6h-4.5z" fill="var(--ink)"/><circle cx="2" cy="6.8" r="1.1" fill="var(--ink)"/><circle cx="8.5" cy="6.8" r="1.1" fill="var(--ink)"/></svg></div>

    <!-- row template values -->
    <div class="row" style="top:33px">
      <span class="cell" style="left:7px">2499</span><span class="cell" style="left:56px">Bramley Asphalt Plant</span><span class="cell" style="left:146px">QTRN - 185 from mm 77 - 98</span><span class="cell" style="left:272px">Harlow Construction - North Division</span>
      <span class="status pending">Pending</span>
      <div class="tons"><div class="bar"><i class="dot" style="width:5px;height:5px"></i></div><div class="tons-meta"><span>00 / 1500</span><span>--</span></div></div>
      <div class="waits">
        <svg width="9" height="8" viewBox="0 0 9 8"><path d="M0 8V2l3 2V2l3 2V0h3v8z" fill="var(--icon)"/></svg><svg width="5" height="4" viewBox="0 0 5 4"><path d="M1 3l1.5-1.5L4 3" stroke="var(--bad)" fill="none"/></svg>
        <svg width="11" height="8" viewBox="0 0 11 8"><path d="M0 1h6.5v5H0zM6.5 2.5h2.5l2 2V6h-4.5z" fill="var(--icon)"/><circle cx="2" cy="6.8" r="1.1" fill="var(--icon)"/><circle cx="8.5" cy="6.8" r="1.1" fill="var(--icon)"/></svg><svg width="5" height="4" viewBox="0 0 5 4"><path d="M1 3l1.5-1.5L4 3" stroke="var(--bad)" fill="none"/></svg>
        <svg width="8" height="10" viewBox="0 0 8 10"><path d="M4 10S0 6 0 4a4 4 0 018 0c0 2-4 6-4 6z" fill="var(--icon)"/><circle cx="4" cy="4" r="1.4" fill="#fff"/></svg><svg width="5" height="4" viewBox="0 0 5 4"><path d="M1 3l1.5-1.5L4 3" stroke="var(--bad)" fill="none"/></svg>
      </div>
      <span class="cell good" style="left:666px">+2 Hrs</span><span class="cell bad" style="left:741px">-15</span>
    </div>

    <div class="row" style="top:66px">
      <span class="cell" style="left:7px">3715</span><span class="cell" style="left:56px">Corwin Asphalt Plant</span><span class="cell" style="left:146px">Maple Ridge</span><span class="cell" style="left:272px">Harlow Construction - North Division</span>
      <span class="status accepted">Accpted</span>
      <div class="tons"><div class="bar"><i style="width:53px"></i></div><div class="tons-meta"><span>750 / 1500</span><span>07:30 - 17:00</span></div></div>
      <span class="cell good" style="left:666px">+2 Hrs</span><span class="cell good" style="left:741px">+12</span>
    </div>

    <div class="row" style="top:99px">
      <span class="cell" style="left:7px">4860</span><span class="cell" style="left:56px">Bramley Asphalt Plant</span><span class="cell" style="left:146px">QTRN - 185 from mm 77 - 98</span><span class="cell" style="left:272px">Harlow Construction - North Division</span>
      <span class="status accepted">Accpted</span>
      <div class="tons"><div class="bar"><i style="width:65px"></i></div><div class="tons-meta"><span>1019 / 1500</span><span>07:30 - 17:00</span></div></div>
      <span class="cell good" style="left:666px">+2 Hrs</span>
    </div>

    <div class="row" style="top:132px">
      <span class="cell" style="left:7px">1612</span><span class="cell" style="left:56px">Tilden Asphalt Plant</span><span class="cell" style="left:146px">B12, Venna Loop, Fairhaven</span><span class="cell" style="left:272px">Harlow Construction - North Division</span>
      <span class="status accepted">Accpted</span>
      <div class="tons"><div class="bar"><i style="width:77px"></i></div><div class="tons-meta"><span>1280 / 1500</span><span>07:30 - 17:00</span></div></div>
      <span class="cell good" style="left:666px">+2 Hrs</span>
    </div>

    <div class="row" style="top:165px">
      <span class="cell" style="left:7px">800</span><span class="cell" style="left:56px">Bramley Asphalt Plant</span><span class="cell" style="left:146px">Maple Ridge</span><span class="cell" style="left:272px">Harlow Construction - North Division</span>
      <span class="status accepted">Accpted</span>
      <div class="tons"><div class="bar"><i style="width:89px"></i></div><div class="tons-meta"><span>1500 / 1500</span><span>07:30 - 17:00</span></div></div>
      <span class="cell good" style="left:666px">+1.5 Hrs</span>
    </div>

    <div class="row" style="top:198px;border-bottom:none">
      <span class="cell" style="left:7px">3236</span><span class="cell" style="left:56px">Corwin Asphalt Plant</span><span class="cell" style="left:146px">Maple Ridge</span><span class="cell" style="left:272px">Harlow Construction - North Division</span>
      <span class="status accepted">Accpted</span>
      <div class="tons"><div class="bar"><i style="width:89px"></i></div><div class="tons-meta"><span>1500 / 1500</span><span>07:30 - 17:00</span></div></div>
      <div class="waits">
        <svg width="9" height="8" viewBox="0 0 9 8"><path d="M0 8V2l3 2V2l3 2V0h3v8z" fill="var(--icon)"/></svg><svg width="5" height="4" viewBox="0 0 5 4"><path d="M1 3l1.5-1.5L4 3" stroke="var(--bad)" fill="none"/></svg>
        <svg width="11" height="8" viewBox="0 0 11 8"><path d="M0 1h6.5v5H0zM6.5 2.5h2.5l2 2V6h-4.5z" fill="var(--icon)"/><circle cx="2" cy="6.8" r="1.1" fill="var(--icon)"/><circle cx="8.5" cy="6.8" r="1.1" fill="var(--icon)"/></svg><svg width="5" height="4" viewBox="0 0 5 4"><path d="M1 3l1.5-1.5L4 3" stroke="var(--bad)" fill="none"/></svg>
        <svg width="8" height="10" viewBox="0 0 8 10"><path d="M4 10S0 6 0 4a4 4 0 018 0c0 2-4 6-4 6z" fill="var(--icon)"/><circle cx="4" cy="4" r="1.4" fill="#fff"/></svg><svg width="5" height="4" viewBox="0 0 5 4"><path d="M1 1l1.5 1.5L4 1" stroke="var(--good)" fill="none"/></svg>
      </div>
      <span class="cell bad" style="left:666px">-00:28 Min</span>
    </div>

    <div class="popup">
      <div class="popup-head">Order # 2499</div>
      <div class="popup-avg">Avg Cycle Time: 02:27</div>
      <div class="popup-line"><span class="name"><svg width="9" height="8" viewBox="0 0 9 8"><path d="M0 8V2l3 2V2l3 2V0h3v8z" fill="var(--brand)"/></svg>Plant (Min)</span><span class="nums">Actual: 33<br>Planned 30</span></div>
      <div class="popup-line"><span class="name"><svg width="11" height="8" viewBox="0 0 11 8"><path d="M0 1h6.5v5H0zM6.5 2.5h2.5l2 2V6h-4.5z" fill="var(--brand)"/><circle cx="2" cy="6.8" r="1.1" fill="var(--brand)"/><circle cx="8.5" cy="6.8" r="1.1" fill="var(--brand)"/></svg>Driving (Min)</span><span class="nums">Actual: 80<br>Planned 60</span></div>
      <div class="popup-line"><span class="name"><svg width="8" height="10" viewBox="0 0 8 10"><path d="M4 10S0 6 0 4a4 4 0 018 0c0 2-4 6-4 6z" fill="var(--brand)"/><circle cx="4" cy="4" r="1.4" fill="#fff"/></svg>Jobsite (Min)</span><span class="nums">Actual: 30<br>Planned 30</span></div>
    </div>

    <nav class="pager">
      <span class="pg prev"><svg width="6" height="6" viewBox="0 0 6 6"><path d="M4 1L2 3l2 2" stroke="#c9c9cf" fill="none"/></svg></span>
      <span class="pg current" style="margin-left:6px">01</span>
      <span class="pg">02</span>
      <span class="pg">03</span>
      <span class="pg">...</span>
      <span class="pg">10</span>
      <span class="pg next" style="margin-left:6px"><svg width="6" height="6" viewBox="0 0 6 6"><path d="M2 1l2 2-2 2" stroke="#fff" fill="none"/></svg></span>
    </nav>
  </section>
</main>
<div class="caption">Dashboard - Details Popup</div>
</body>
</html>
```